Stationary for 2-office law firm with global theme

I need stationary with contact info for two offices. I'd like the same letterhead design to work for printing on stationary and also for digital use in Word. The colors and feel should match the new logo, which is a stylized globe with and "F" in it. I'd also like envelopes with an eye-catching design.

Target Market(s)

U.S. citizens seeking dual citizenship with Italy or Ireland

Industry/Entity Type

Law

Font styles to use
Serif
Sans Serif
Other font styles liked:
• To match the logo?

Colors
0054AA
0677BA
7BADD7
CADEEF
E8F1F8

Requirements
Must have
• Clean, modern design incorporating new logo

```html
<!DOCTYPE html>
<html lang="en">
<head>
<meta charset="utf-8">
<title>Varenna Law Stationery</title>
<link href="https://fonts.googleapis.com/css2?family=Montserrat:wght@400;500;600;700&display=swap" rel="stylesheet">
<style>
  :root{
    --sky:#0aa4e6;
    --blue:#0677ba;
    --royal:#0054aa;
    --navy:#06345f;
    --ink:#1f3550;
    --text:#555b63;
    --paper:#ffffff;
    --board:#e9eaeb;
    --rule:#cfd3d8;
  }
  *{box-sizing:border-box;margin:0;padding:0}
  html,body{width:675px;height:1200px;overflow:hidden}
  body{background:var(--board);font-family:'Montserrat',sans-serif;color:var(--text);position:relative}

  .board-wave{position:absolute;left:0;bottom:0;width:675px;height:560px}

  .section-title{position:absolute;color:var(--sky);font-weight:600;line-height:1.2}
  .title-letterhead{left:32px;top:52px;font-size:25px}
  .title-envelope{left:438px;top:188px;font-size:11px}
  .title-card{left:438px;top:428px;font-size:19px}

  /* brand lockup */
  .brand{display:flex;align-items:center;gap:6px}
  .brand-dot{border-radius:50%;background:var(--royal);flex:none}
  .brand-name{font-weight:700;color:var(--ink);letter-spacing:.2px;line-height:1}

  .contact{list-style:none;font-weight:600;color:var(--ink)}
  .contact li{display:flex;align-items:flex-start;gap:4px}
  .contact svg{flex:none;fill:var(--sky)}

  /* letterhead */
  .letterhead{position:absolute;left:32px;top:140px;width:400px;height:566px;background:var(--paper);overflow:hidden;box-shadow:0 2px 8px rgba(0,0,0,.06)}
  .letterhead .brand{position:absolute;left:44px;top:22px}
  .letterhead .brand-dot{width:22px;height:22px}
  .letterhead .brand-name{font-size:12.5px}
  .letterhead .contact{position:absolute;left:316px;top:20px;font-size:3.8px;line-height:1.35}
  .letterhead .contact li{margin-bottom:3px}
  .lh-rule{position:absolute;left:44px;right:24px;top:60px;height:1px;background:var(--rule)}
  .recipient{position:absolute;left:46px;top:89px;font-size:7px;line-height:1.5}
  .recipient .name{color:var(--sky);font-weight:600}
  .lh-body{position:absolute;left:46px;top:148px;width:330px;font-size:6.9px;line-height:1.3;text-align:justify}
  .signoff{position:absolute;left:46px;top:372px;font-size:7px}
  .signature{position:absolute;left:46px;top:408px;width:77px;border-top:1px solid var(--text);padding-top:2px;font-size:7px;line-height:1.3}
  .signature .name{color:var(--sky);font-weight:600}
  .lh-footer{position:absolute;left:0;bottom:0;width:400px;height:80px}

  /* envelope */
  .envelope-back{position:absolute;left:475px;top:220px;width:173px;height:130px;background:var(--paper)}
  .envelope-flap{position:absolute;left:0;top:0;width:173px;height:55px}
  .envelope-front{position:absolute;left:438px;top:262px;width:180px;height:94px;background:#f4f5f6;overflow:hidden;box-shadow:0 2px 6px rgba(0,0,0,.08)}
  .envelope-front .brand{position:absolute;left:7px;top:9px}
  .envelope-front .brand-dot{width:12px;height:12px}
  .envelope-front .brand-name{font-size:7px}
  .envelope-front .contact{position:absolute;left:11px;top:52px;font-size:2.6px;line-height:1.3}
  .envelope-front .contact li{margin-bottom:1.5px}
  .env-wave{position:absolute;left:0;bottom:0;width:180px;height:52px}
  .env-window{position:absolute;left:85px;top:45px;width:80px;height:34px;border-radius:3px;background:linear-gradient(135deg,#e3e5e7,#c4c8cc 45%,#eceef0);border:1px solid #d5d8db}

  /* business card */
  .card-front{position:absolute;left:438px;top:468px;width:200px;height:114px;background:var(--sky);display:flex;flex-direction:column;align-items:center;justify-content:center;gap:6px}
  .card-front::after{content:"";position:absolute;left:0;right:0;bottom:0;height:6px;background:var(--navy)}
  .card-front .brand-dot{width:30px;height:30px;background:#fff}
  .card-front .brand-name{color:#fff;font-size:15px}

  .card-back{position:absolute;left:348px;top:760px;width:290px;height:164px;background:var(--paper);overflow:hidden;box-shadow:0 6px 14px rgba(0,0,0,.18)}
  .card-back .brand{position:absolute;left:26px;top:60px;flex-direction:column;gap:6px}
  .card-back .brand-dot{width:26px;height:26px}
  .card-back .brand-name{font-size:12px}
  .card-divider{position:absolute;left:138px;top:14px;width:1px;height:96px;background:var(--rule)}
  .person{position:absolute;left:152px;top:50px}
  .person-name{font-size:10px;color:var(--ink);font-weight:500}
  .person-name strong{font-weight:700}
  .person-role{font-size:4px;font-weight:600;color:var(--ink);margin-top:2px;margin-bottom:8px}
  .card-back .contact{font-size:4.4px;line-height:1.3}
  .card-back .contact li{margin-bottom:4px}
  .card-wave{position:absolute;left:0;bottom:0;width:290px;height:48px}
</style>
</head>
<body>

<svg class="board-wave" viewBox="0 0 675 560" preserveAspectRatio="none" aria-hidden="true">
  <path d="M0 560 L0 530 C200 520 330 490 420 400 C520 300 580 250 675 238 L675 560 Z" fill="#0d8cd0"/>
  <path d="M0 560 L0 530 C230 525 360 495 450 400 C540 310 600 280 675 272 L675 560 Z" fill="var(--navy)"/>
  <rect x="0" y="518" width="675" height="42" fill="#042b4f"/>
</svg>

<h1 class="section-title title-letterhead">Letterhead Design a4<br>word document</h1>

<article class="letterhead">
  <div class="brand"><span class="brand-dot"></span><span class="brand-name">VARENNA LAW</span></div>
  <ul class="contact">
    <li><svg width="5" height="4" viewBox="0 0 10 8"><rect width="10" height="8" rx="1"/></svg>info@loremipsumdolor</li>
    <li><svg width="5" height="5" viewBox="0 0 10 10"><path d="M5 0a4 4 0 0 1 4 4c0 3-4 6-4 6S1 7 1 4a4 4 0 0 1 4-4z"/></svg>Dummy Road 125x<br>Street Location, City, Area</li>
    <li><svg width="5" height="5" viewBox="0 0 10 10"><path d="M2 0l2 2-1 2c1 1 2 2 3 3l2-1 2 2-2 2C4 10 0 6 0 2z"/></svg>+00 1234 5678 9012<br>+00 1234 5678 9012</li>
  </ul>
  <div class="lh-rule"></div>

  <div class="recipient">
    <div>To :</div>
    <div class="name">Mr Jane Doe</div>
    <div>Lorem ipsum</div>
  </div>

  <div class="lh-body">
    <p>Lorem ipsum dolor sit amet, consectetuer adipiscing elit, sed diam nonummy nibh euismod tincidunt ut laoreet dolore magna aliquam erat volutpat. Ut wisi enim ad minim veniam, quis nostrud exerci tation ullamcorper suscipit lobortis nisl ut aliquip ex ea commodo consequat. Duis autem vel eum iriure dolor in hendrerit in vulputate velit esse molestie consequat, vel illum dolore eu feugiat nulla facilisis at vero eros et accumsan et iusto odio dignissim qui blandit praesent luptatum zzril delenit augue duis dolore te feugait nulla facilisi.</p>
    <p>Lorem ipsum dolor sit amet, cons ectetuer adipiscing elit, sed diam nonummy nibh euismod tincidunt ut laoreet dolore magna aliquam erat volutpat. Ut wisi enim ad minim veniam, quis nostrud exerci tation ullamcorper suscipit lobortis nisl ut aliquip ex ea commodo consequat.</p>
    <p>Lorem ipsum dolor sit amet, consectetuer adipiscing elit, sed diam nonummy nibh euismod tincidunt ut laoreet dolore magna aliquam erat volutpat. Ut wisi enim ad minim veniam, quis nostrud exerci tation ullamcorper suscipit lobortis nisl ut aliquip ex ea commodo consequat. Duis autem vel eum iriure dolor in hendrerit in vulputate velit esse molestie consequat, vel illum dolore eu feugiat nulla facilisis at vero eros et accumsan et iusto odio dignissim qui blandit praesent luptatum zzril delenit augue duis dolore te feugait nulla facilisi.</p>
    <p>Lorem ipsum dolor sit amet, cons ectetuer adipiscing elit, sed diam nonummy nibh euismod tincidunt ut laoreet dolore magna aliquam erat volutpat. Ut wisi enim ad minim veniam, quis nostrud exerci tation ullamcorper suscipit lobortis nisl ut aliquip ex ea</p>
  </div>

  <p class="signoff">Best Regards.</p>
  <div class="signature"><div class="name">Sample Name</div><div>Director</div></div>

  <svg class="lh-footer" viewBox="0 0 400 80" preserveAspectRatio="none" aria-hidden="true">
    <path d="M0 40 L230 40 C290 40 310 8 400 0 L400 80 L0 80 Z" fill="var(--blue)"/>
    <path d="M0 40 L240 40 C300 40 320 20 400 16 L400 80 L0 80 Z" fill="var(--sky)"/>
    <path d="M0 56 L250 56 C310 56 330 30 400 26 L400 80 L0 80 Z" fill="var(--navy)"/>
  </svg>
</article>

<h2 class="section-title title-envelope">Envelope Design :</h2>

<div class="envelope-back">
  <svg class="envelope-flap" viewBox="0 0 173 55" preserveAspectRatio="none" aria-hidden="true">
    <path d="M10 0 H158 C166 0 168 6 173 22 L160 48 C157 53 150 55 140 55 H30 C20 55 14 50 10 45 L0 22 Z" fill="var(--navy)"/>
    <path d="M0 22 L10 45 C14 50 20 55 30 55 H140 C150 55 157 53 160 48 L173 22 Z" fill="#04223f" opacity=".6"/>
  </svg>
</div>

<div class="envelope-front">
  <div class="brand"><span class="brand-dot"></span><span class="brand-name">VARENNA LAW</span></div>
  <ul class="contact">
    <li><svg width="3" height="3" viewBox="0 0 10 8"><rect width="10" height="8" rx="1"/></svg>info@loremipsumdolor</li>
    <li><svg width="3" height="3" viewBox="0 0 10 10"><path d="M5 0a4 4 0 0 1 4 4c0 3-4 6-4 6S1 7 1 4a4 4 0 0 1 4-4z"/></svg>Dummy Road 125x<br>Street Location, City, Area</li>
    <li><svg width="3" height="3" viewBox="0 0 10 10"><path d="M2 0l2 2-1 2c1 1 2 2 3 3l2-1 2 2-2 2C4 10 0 6 0 2z"/></svg>+00 1234 5678 9012<br>+00 1234 5678 9012</li>
  </ul>
  <svg class="env-wave" viewBox="0 0 180 52" preserveAspectRatio="none" aria-hidden="true">
    <path d="M0 36 L90 36 C130 36 140 4 180 0 L180 52 L0 52 Z" fill="var(--sky)"/>
    <path d="M0 40 L95 40 C135 40 145 8 180 6 L180 52 L0 52 Z" fill="var(--navy)"/>
    <rect x="0" y="41" width="100" height="2" fill="#fff"/>
  </svg>
  <div class="env-window"></div>
</div>

<h2 class="section-title title-card">Business Card</h2>

<div class="card-front">
  <span class="brand-dot"></span>
  <span class="brand-name">VARENNA LAW</span>
</div>

<div class="card-back">
  <div class="brand"><span class="brand-dot"></span><span class="brand-name">VARENNA LAW</span></div>
  <div class="card-divider"></div>
  <div class="person">
    <div class="person-name">DANIEL <strong>REED CARTER</strong></div>
    <div class="person-role">CO-FOUNDER BUSINESS NAME</div>
    <ul class="contact">
      <li><svg width="4" height="4" viewBox="0 0 10 10"><path d="M5 0a4 4 0 0 1 4 4c0 3-4 6-4 6S1 7 1 4a4 4 0 0 1 4-4z" fill="var(--ink)"/></svg>123 Dummy Road, Lorem Ipsum, Country</li>
      <li><svg width="4" height="4" viewBox="0 0 10 10"><path d="M2 0l2 2-1 2c1 1 2 2 3 3l2-1 2 2-2 2C4 10 0 6 0 2z" fill="var(--ink)"/></svg>+00 1234 5678 9012</li>
      <li><svg width="4" height="4" viewBox="0 0 10 8"><rect width="10" height="8" rx="1" fill="var(--ink)"/></svg>contact@loremipsumdolor</li>
      <li><svg width="4" height="4" viewBox="0 0 10 10"><circle cx="5" cy="5" r="5" fill="var(--ink)"/></svg>www.loremipsumdolor</li>
    </ul>
  </div>
  <svg class="card-wave" viewBox="0 0 290 48" preserveAspectRatio="none" aria-hidden="true">
    <path d="M0 30 L200 30 C240 30 250 8 290 6 L290 48 L0 48 Z" fill="var(--sky)"/>
    <path d="M0 30 L210 30 C235 30 245 24 255 18 C245 32 230 36 210 36 L0 36 Z" fill="var(--navy)"/>
  </svg>
</div>

</body>
</html>
```